Boutique Real Estate Brokerage looking for business card, letterhead and envelope design

We are looking for a cohesive design for our business cards, letterhead and envelopes and that mirrors our high-end homes and clientele. Fern & Gable is being launched and designed for the marketplace of tomorrow. We grew from the #1 team in our community into a full-service firm that is going to revolutionize the traditional real estate model.

We understand that it’s more important than ever to help our clients and partners adapt to behavioral and market changes being driven by generational shifts and technological advances in society, and by combining traditional brokerage services with innovative production and marketing capabilities, we know how to do that better than anyone else.

Requirements
Must have
• business card, letterhead and envelope design - attached logo.

```html
<!DOCTYPE html>
<html lang="en">
<head>
<meta charset="utf-8">
<title>Fern &amp; Gable Stationery</title>
<link href="https://fonts.googleapis.com/css2?family=Lato:wght@400;700;900&family=Encode+Sans+Condensed:wght@300;400&display=swap" rel="stylesheet">
<style>
  :root{
    --navy:#150a52;
    --gold:#c08545;
    --ink:#4f4f57;
    --paper:#ffffff;
    --backdrop:#d9e4ef;
  }
  *{margin:0;padding:0;box-sizing:border-box}
  html,body{width:1200px;height:831px;overflow:hidden}
  body{background:var(--backdrop);position:relative;font-family:"Lato",sans-serif;color:var(--navy)}
  .sheet{position:absolute;background:var(--paper);box-shadow:0 2px 8px rgba(40,50,80,.28);overflow:hidden}
  .wave{position:absolute;left:0;bottom:0;width:100%;display:block}
  .brand{position:absolute;display:flex;align-items:center;font-family:"Lato",sans-serif;font-weight:900;color:var(--navy);white-space:nowrap;letter-spacing:.02em}
  .brand-mark{display:block;background:var(--gold);margin-right:.45em}
  .contact{position:absolute;font-family:"Lato",sans-serif;color:var(--navy);white-space:nowrap}
  .contact .line{display:flex;align-items:center}
  .contact .ico{fill:none;stroke:var(--gold);stroke-width:1.6;flex:none}
  .contact .accent{color:var(--gold)}

  /* Letterhead */
  .letterhead{left:117px;top:111px;width:430px;height:609px}
  .letterhead .brand{left:40px;top:43px;font-size:16.5px}
  .letterhead .brand-mark{width:30px;height:34px}
  .letterhead .contact{left:314px;top:31px;font-size:8px;line-height:9.6px}
  .letterhead .contact .gap{height:4px}
  .letterhead .contact .line{margin-bottom:1.6px}
  .letterhead .contact .ico{width:8px;height:8px;margin-right:6px}
  .letter-body{position:absolute;left:40px;top:199px;width:349px;font-family:"Encode Sans Condensed",sans-serif;font-weight:300;font-size:9.6px;line-height:15px;color:var(--ink);text-align:justify}
  .letter-body p{margin-bottom:15px}
  .letter-body .sign-off{margin-top:22px;margin-bottom:6px}
  .signature{display:block;width:36px;height:22px;background:#e6e4f0;border-radius:3px}

  /* Business cards */
  .card-front{left:635px;top:112px;width:182px;height:104px}
  .card-front .brand{left:12px;top:44px;font-size:7px}
  .card-front .brand-mark{width:11px;height:13px}
  .card-front .divider{position:absolute;left:88px;top:27px;width:1px;height:50px;background:var(--navy)}
  .card-front .person{position:absolute;left:100px;top:25px;font-size:8.2px;font-weight:900;letter-spacing:.01em}
  .card-front .person span{color:var(--gold)}
  .card-front .role{position:absolute;left:100px;top:35px;font-size:4.6px}
  .card-front .contact{left:100px;top:45px;font-size:4.4px;line-height:5.6px}
  .card-front .contact .gap{height:2px}
  .card-front .contact .line{margin-bottom:1.2px}
  .card-front .contact .ico{width:4.5px;height:4.5px;margin-right:4px}

  .card-back{left:904px;top:111px;width:182px;height:104px;background:var(--navy)}
  .card-back .brand{left:37px;top:41px;font-size:11px;color:#fff}
  .card-back .brand-mark{width:18px;height:22px}

  /* Envelopes */
  .envelope-back{left:635px;top:248px;width:451px;height:226px}
  .envelope-back .flap{position:absolute;left:0;top:0;width:451px;height:66px;display:block}
  .envelope-back .brand{left:0;width:451px;justify-content:center;top:24px;font-size:14px;color:var(--gold)}

  .envelope-front{left:635px;top:494px;width:451px;height:226px}
  .envelope-front .brand{left:42px;top:46px;font-size:16.5px}
  .envelope-front .brand-mark{width:30px;height:34px}
  .envelope-front .contact{left:42px;top:133px;font-size:8px;line-height:9.6px}
  .envelope-front .contact .gap{height:4px}
  .envelope-front .contact .line{margin-bottom:1.6px}
  .envelope-front .contact .ico{width:8px;height:8px;margin-right:6px}
</style>
</head>
<body>
<svg width="0" height="0" style="position:absolute" aria-hidden="true">
  <defs>
    <symbol id="icon-phone" viewBox="0 0 16 16"><path d="M4 1.5l2.5 3-1.5 2a8 8 0 0 0 4.5 4.5l2-1.5 3 2.5-1.5 2.5C7 14.5 1.5 9 1.5 3z"/></symbol>
    <symbol id="icon-mail" viewBox="0 0 16 16"><rect x="1.5" y="3.5" width="13" height="9"/><path d="M1.5 3.5l6.5 5.5 6.5-5.5"/></symbol>
    <symbol id="icon-globe" viewBox="0 0 16 16"><circle cx="8" cy="8" r="6.5"/><ellipse cx="8" cy="8" rx="3" ry="6.5"/><path d="M1.5 8h13"/></symbol>
  </defs>
</svg>

<!-- Letterhead -->
<section class="sheet letterhead">
  <div class="brand"><span class="brand-mark"></span>Fern &amp; Gable</div>
  <div class="contact">
    <div>1234 First Line Address</div>
    <div>5678 Second Line Address</div>
    <div class="gap"></div>
    <div class="line"><svg class="ico"><use href="#icon-phone"/></svg>(555) 214-0390</div>
    <div class="line"><svg class="ico"><use href="#icon-mail"/></svg>info@yourmail.com</div>
    <div class="line"><svg class="ico"><use href="#icon-globe"/></svg>www.<span class="accent">yourwebsite</span>.com</div>
  </div>
  <div class="letter-body">
    <p>Dear Sir/Mam,</p>
    <p>Contrary to popular belief, Lorem Ipsum is not simply random text. It has roots in a piece of classical Latin literature from 45 BC, making it over 2000 years old. Daniel Whitcombe, a Latin professor at Ashgrove College in Virginia, looked up one of the more obscure Latin words, consectetur.</p>
    <p>Lorem Ipsum comes from sections 1.10.32 and 1.10.33 of "de Finibus Bonorum et Malorum" (The Extremes of Good and Evil) by Quintus Aurelian, written in 45 BC. This book is a treatise on the theory of ethics, very popular during the Renaissance. The first line of Lorem Ipsum.</p>
    <p>The standard chunk of Lorem Ipsum used since the 1500s is reproduced below for those interested. Sections 1.10.32 and 1.10.33 from "de Finibus Bonorum et Malorum" by Quintus Aurelian are also reproduced in their exact original.</p>
    <p>The standard chunk of Lorem Ipsum used since the 1500s is reproduced below for those interested.</p>
    <p class="sign-off">Best Regards</p>
    <span class="signature" role="img" aria-label="Handwritten signature"></span>
  </div>
  <svg class="wave" viewBox="0 0 430 30" height="30" preserveAspectRatio="none" aria-hidden="true">
    <path d="M0 11 Q215 -11 430 11" fill="none" stroke="var(--gold)" stroke-width="1.6"/>
    <path d="M0 17 Q215 -2 430 17 L430 30 L0 30Z" fill="var(--navy)"/>
  </svg>
</section>

<!-- Business card, front -->
<section class="sheet card-front">
  <div class="brand"><span class="brand-mark"></span>Fern &amp; Gable</div>
  <div class="divider"></div>
  <div class="person">OWEN <span>HARTLEY</span></div>
  <div class="role">Founder &amp; CEO</div>
  <div class="contact">
    <div>1234 First Line Address</div>
    <div>5678 Second Line Address</div>
    <div class="gap"></div>
    <div class="line"><svg class="ico"><use href="#icon-phone"/></svg>(555) 214-0390</div>
    <div class="line"><svg class="ico"><use href="#icon-mail"/></svg>info@yourmail.com</div>
    <div class="line"><svg class="ico"><use href="#icon-globe"/></svg>www.<span class="accent">yourwebsite</span>.com</div>
  </div>
  <svg class="wave" viewBox="0 0 182 11" height="11" preserveAspectRatio="none" aria-hidden="true">
    <path d="M0 4 Q91 -3 182 4" fill="none" stroke="var(--gold)" stroke-width="0.9"/>
    <path d="M0 6.5 Q91 1 182 6.5 L182 11 L0 11Z" fill="var(--navy)"/>
  </svg>
</section>

<!-- Business card, back -->
<section class="sheet card-back">
  <div class="brand"><span class="brand-mark"></span>Fern &amp; Gable</div>
</section>

<!-- Envelope, back -->
<section class="sheet envelope-back">
  <svg class="flap" viewBox="0 0 451 66" aria-hidden="true">
    <path d="M0 0 H451 L447 36 Q444 66 414 66 H37 Q7 66 4 36Z" fill="var(--navy)"/>
  </svg>
  <div class="brand">Fern &amp; Gable</div>
</section>

<!-- Envelope, front -->
<section class="sheet envelope-front">
  <div class="brand"><span class="brand-mark"></span>Fern &amp; Gable</div>
  <div class="contact">
    <div>1234 First Line Address</div>
    <div>5678 Second Line Address</div>
    <div class="gap"></div>
    <div class="line"><svg class="ico"><use href="#icon-phone"/></svg>(555) 214-0390</div>
    <div class="line"><svg class="ico"><use href="#icon-mail"/></svg>info@yourmail.com</div>
    <div class="line"><svg class="ico"><use href="#icon-globe"/></svg>www.<span class="accent">yourwebsite</span>.com</div>
  </div>
  <svg class="wave" viewBox="0 0 451 29" height="29" preserveAspectRatio="none" aria-hidden="true">
    <path d="M0 10 Q225 -10 451 10" fill="none" stroke="var(--gold)" stroke-width="1.6"/>
    <path d="M0 16 Q225 -2 451 16 L451 29 L0 29Z" fill="var(--navy)"/>
  </svg>
</section>
</body>
</html>
```